Website Upgrade

Create new look for existing website: www.lunarisgrove.ca . You will find details on what we are about on the website. Email us at lunaris.grove@mailbright.ca if you have any questions. We will be more than happy to answer.
Lunaris grove is a website for women focused on empowering women.
Website must:
1. Be able to stream videos
2. Use of blogs
3. Purple must be one of the colours used in the scheme.
4. Must use existing lunaris grove logo (purple head with 'Lunaris Grove' script in white.. see on homepage). However, we are open to new logo suggestions
5. Must be professional. We are trendy but not boring.

```html
<!DOCTYPE html>
<html lang="en">
<head>
<meta charset="utf-8">
<title>Lunaris Grove</title>
<link href="https://fonts.googleapis.com/css2?family=Didact+Gothic&family=Arimo:wght@400;700&family=Lato:wght@700;900&display=swap" rel="stylesheet">
<style>
:root{
  --plum:#9a0a6e;
  --plum-dark:#7d0a5c;
  --magenta:#b0107f;
  --red:#e8202a;
  --text:#4a4a4a;
  --muted:#8a8a8a;
  --white:#ffffff;
  --line:#d8d8d8;
}
*{margin:0;padding:0;box-sizing:border-box}
html,body{width:933px;height:1200px;overflow:hidden;background:var(--white)}
body{position:relative;font-family:"Arimo",Arial,sans-serif;color:var(--text)}
.abs{position:absolute}

/* top nav */
.topbar{left:0;top:0;width:933px;height:38px;background:var(--plum)}
.brand-sm{left:135px;top:11px;font-family:"Didact Gothic",sans-serif;font-size:14px;color:var(--white);letter-spacing:.5px;display:flex;align-items:center;gap:6px}
.brand-sm .dot{width:9px;height:9px;border-radius:50%;background:var(--white)}
.nav a{position:absolute;top:14px;font-family:"Didact Gothic",sans-serif;font-size:10px;color:#f1c9e3;text-decoration:none;letter-spacing:-.2px}
.nav a.on{color:var(--white);font-weight:bold}
.social-top span{position:absolute;top:13px;width:14px;height:14px;border-radius:2px}
.search{left:777px;top:13px}

/* hero */
.hero{left:0;top:38px;width:933px;height:337px;background:linear-gradient(180deg,#cfd9e2 0%,#e6eaee 45%,#f2f2ef 60%,#b9c9cf 70%,#cdc9c2 85%,#a9a49d 100%)}
.hero-brand{left:250px;top:178px;width:432px;text-align:center;font-family:"Didact Gothic",sans-serif;font-size:40px;color:var(--magenta);letter-spacing:1px;display:flex;align-items:center;justify-content:center;gap:12px}
.hero-brand .dot{width:18px;height:18px;border-radius:50%;background:var(--magenta);flex:none}
.hero-btn{left:511px;top:251px;width:170px;height:27px;border:1.5px solid var(--magenta);background:rgba(255,255,255,.75);color:var(--magenta);font-family:"Didact Gothic",sans-serif;font-size:13px;text-align:center;line-height:24px}
.arrow{top:191px;width:27px;height:27px;border-radius:50%}

/* video */
.video{left:144px;top:387px;width:414px;height:232px;background:linear-gradient(180deg,#4f6a86 0%,#8aa0b1 40%,#d9a35a 75%,#5a4a2c 100%)}
.ctrl-icon{width:22px;height:22px;background:rgba(40,40,40,.75);border-radius:2px;left:382px}
.play-box{left:16px;top:197px;width:43px;height:30px;background:#1b1b1b}
.seek{left:63px;top:208px;width:272px;height:6px;background:#1c1c1c;border:1px solid #555}
.time{left:57px;top:196px;font-size:7px;background:#fff;color:#222;padding:0 2px}
.hd{left:364px;top:205px;font:bold italic 11px "Arimo",sans-serif;color:#17a7e0}

/* promo */
.promo{left:563px;top:387px;width:227px;height:107px;background:linear-gradient(135deg,#a8127d 0%,#c21d86 60%,#d9559c 100%)}
.promo h2{position:absolute;left:9px;top:10px;font-family:"Didact Gothic",sans-serif;font-weight:normal;font-size:19px;line-height:21.5px;color:var(--white);letter-spacing:-.3px}
.promo-cta{left:563px;top:494px;width:227px;height:38px;background:linear-gradient(180deg,#f03a2e,#c9142a);border-bottom:3px solid #a8127d}
.promo-cta span{position:absolute;left:12px;top:11px;font-family:"Didact Gothic",sans-serif;font-size:13px;color:var(--white)}

/* thumbs */
.thumb{width:204px;height:113px}
.play-ring{position:absolute;left:87px;top:41px}

/* posts */
.posts-title{left:563px;top:548px;font-family:"Didact Gothic",sans-serif;font-size:20px;color:var(--magenta);letter-spacing:-.5px}
.post{left:564px;width:226px}
.post .meta{font-size:8px;color:var(--muted)}
.post .meta b{color:#222}
.post h3{font-family:"Didact Gothic",sans-serif;font-weight:normal;font-size:11px;color:var(--muted);margin:3px 0 2px}
.post h3.hot{color:var(--red)}
.post p{font-size:8px;line-height:9.6px;color:#555}

/* band */
.band{left:0;top:886px;width:933px;height:76px;background:linear-gradient(100deg,#8f1270 0%,#a41a80 50%,#8c0f6c 100%)}
.band h2{position:absolute;left:154px;top:27px;font-family:"Lato",sans-serif;font-weight:700;font-size:16px;color:var(--white)}
.band-btn{left:610px;top:22px;width:167px;height:32px;border:1px solid var(--white);color:var(--white);font-family:"Lato",sans-serif;font-weight:900;font-size:11px;text-align:center;line-height:30px}

/* footer */
.foot-brand{left:144px;top:1024px;font-family:"Didact Gothic",sans-serif;font-size:27px;color:var(--magenta);display:flex;align-items:center;gap:10px;letter-spacing:.5px}
.foot-brand .dot{width:14px;height:14px;border-radius:50%;background:var(--magenta)}
.recent-title{left:493px;top:998px;font-family:"Arimo",sans-serif;font-weight:700;font-size:10px;color:#333}
.recent a{position:absolute;font-size:7.5px;color:#666;text-decoration:none}
.divider{left:133px;top:1153px;width:667px;height:1px;background:var(--line)}
.copy{left:147px;top:1171px;font-size:8px;color:#444}
.foot-nav a{position:absolute;top:1171px;font-size:8.5px;color:#444;text-decoration:none}
.foot-nav a.on{color:var(--magenta)}
.social-foot span{position:absolute;top:1166px;width:19px;height:19px;border-radius:3px}
</style>
</head>
<body>

<header>
  <div class="abs topbar"></div>
  <div class="abs brand-sm"><span class="dot"></span>Lunaris Grove</div>
  <nav class="nav">
    <a class="on" style="left:306px">HOME</a>
    <a style="left:371px">LUNARIS GROVE</a>
    <a style="left:491px">BLOG</a>
    <a style="left:553px">OUR BIOS</a>
    <a style="left:634px">CONTACT US</a>
  </nav>
  <div class="social-top" aria-label="Social links">
    <span style="left:711px;background:#4a6db3"></span>
    <span style="left:729px;background:#3aa4dc"></span>
    <span style="left:748px;background:#d8262c"></span>
  </div>
  <svg class="abs search" width="14" height="14" viewBox="0 0 14 14" aria-label="Search"><circle cx="6" cy="6" r="4.5" fill="none" stroke="#fff" stroke-width="1.4"/><line x1="9.3" y1="9.3" x2="13" y2="13" stroke="#fff" stroke-width="1.5"/></svg>
</header>

<section>
  <div class="abs hero" role="img" aria-label="Woman meditating cross-legged on a wooden pier by the sea under a bright cloudy sky"></div>
  <div class="abs hero-brand"><span class="dot"></span>Lunaris Grove</div>
  <div class="abs hero-btn">Contact Now!</div>
  <svg class="abs arrow" style="left:106px" viewBox="0 0 27 27" aria-label="Previous slide"><circle cx="13.5" cy="13.5" r="13.5" fill="#a3207b"/><polyline points="15.5,8 10,13.5 15.5,19" fill="none" stroke="#fff" stroke-width="2"/></svg>
  <svg class="abs arrow" style="left:799px" viewBox="0 0 27 27" aria-label="Next slide"><circle cx="13.5" cy="13.5" r="13.5" fill="#9a9a9a" opacity=".6"/><polyline points="11.5,8 17,13.5 11.5,19" fill="none" stroke="#fff" stroke-width="2"/></svg>
</section>

<main>
  <div class="abs video" role="img" aria-label="Video still: silhouette of a woman leaping against a sunset sky">
    <div class="abs ctrl-icon" style="top:12px"></div>
    <div class="abs ctrl-icon" style="top:40px"></div>
    <div class="abs ctrl-icon" style="top:67px"></div>
    <svg class="abs" style="left:388px;top:18px" width="10" height="10" viewBox="0 0 10 10"><path d="M5 9 L1 5 A2.3 2.3 0 0 1 5 2 A2.3 2.3 0 0 1 9 5 Z" fill="#fff"/></svg>
    <svg class="abs" style="left:387px;top:45px" width="12" height="12" viewBox="0 0 12 12"><circle cx="6" cy="6" r="5" fill="none" stroke="#fff" stroke-width="1.3"/><polyline points="6,3 6,6 8,7" fill="none" stroke="#fff" stroke-width="1.2"/></svg>
    <svg class="abs" style="left:387px;top:72px" width="12" height="12" viewBox="0 0 12 12"><polygon points="1,6 11,1 7,11 6,7" fill="#fff"/></svg>
    <div class="abs play-box"></div>
    <svg class="abs" style="left:31px;top:205px" width="12" height="14" viewBox="0 0 12 14"><polygon points="0,0 12,7 0,14" fill="#fff"/></svg>
    <div class="abs time">00:00</div>
    <div class="abs seek"></div>
    <svg class="abs" style="left:343px;top:208px" width="16" height="8" viewBox="0 0 16 8"><g fill="#17a7e0"><rect x="0" width="2" height="8"/><rect x="3.5" width="2" height="8"/><rect x="7" width="2" height="8"/><rect x="10.5" width="2" height="8"/><rect x="14" width="2" height="8"/></g></svg>
    <div class="abs hd">HD</div>
    <svg class="abs" style="left:388px;top:208px" width="9" height="9" viewBox="0 0 9 9"><g stroke="#fff" stroke-width="1.4"><line x1="0" y1="0" x2="3" y2="3"/><line x1="9" y1="0" x2="6" y2="3"/><line x1="0" y1="9" x2="3" y2="6"/><line x1="9" y1="9" x2="6" y2="6"/></g></svg>
  </div>

  <div class="abs promo" role="img" aria-label="Woman with arms raised in magenta light">
    <h2>EMBODY YOUR<br>RADIANCE,<br>MAGNETISM, AND<br>FEMININE POWER NOW</h2>
  </div>
  <div class="abs promo-cta">
    <span>CONTACT NOW!</span>
    <svg class="abs" style="left:192px;top:11px" width="22" height="14" viewBox="0 0 22 14"><rect x=".7" y=".7" width="20.6" height="12.6" rx="1.5" fill="none" stroke="#fff" stroke-width="1.2"/><polyline points="1,1 11,8 21,1" fill="none" stroke="#fff" stroke-width="1.2"/></svg>
  </div>

  <div class="abs thumb" style="left:144px;top:626px;background:linear-gradient(135deg,#3d6b1f,#8cb54a 50%,#2f5a1a)" role="img" aria-label="Video thumbnail: woman with open arms among green trees"><svg class="play-ring" width="30" height="30" viewBox="0 0 30 30"><circle cx="15" cy="15" r="13" fill="rgba(0,0,0,.15)" stroke="#fff" stroke-width="2.5"/><polygon points="12,9 21,15 12,21" fill="#fff"/></svg></div>
  <div class="abs thumb" style="left:355px;top:626px;background:linear-gradient(180deg,#5d7a9a,#8aa3bc 60%,#6c86a3)" role="img" aria-label="Video thumbnail: dancer leaping against a blue sky"><svg class="play-ring" width="30" height="30" viewBox="0 0 30 30"><circle cx="15" cy="15" r="13" fill="rgba(0,0,0,.15)" stroke="#fff" stroke-width="2.5"/><polygon points="12,9 21,15 12,21" fill="#fff"/></svg></div>
  <div class="abs thumb" style="left:144px;top:746px;background:linear-gradient(135deg,#cfd3d6,#e2e2e0 50%,#b8bec2)" role="img" aria-label="Video thumbnail: portrait of a smiling woman"><svg class="play-ring" width="30" height="30" viewBox="0 0 30 30"><circle cx="15" cy="15" r="13" fill="rgba(0,0,0,.15)" stroke="#fff" stroke-width="2.5"/><polygon points="12,9 21,15 12,21" fill="#fff"/></svg></div>
  <div class="abs thumb" style="left:355px;top:746px;background:linear-gradient(135deg,#3c3c3c,#8b8b8b 50%,#5a5a5a)" role="img" aria-label="Video thumbnail: businesswoman running from crumbling blocks"><svg class="play-ring" width="30" height="30" viewBox="0 0 30 30"><circle cx="15" cy="15" r="13" fill="rgba(0,0,0,.15)" stroke="#fff" stroke-width="2.5"/><polygon points="12,9 21,15 12,21" fill="#fff"/></svg></div>

  <h2 class="abs posts-title">POPULAR POSTS</h2>
  <article class="abs post" style="top:578px">
    <div class="meta"><b>Lorem</b> | June 5, 2014 3:26 am</div>
    <h3 class="hot">VIDEO: Lorem ipsum dolor</h3>
    <p>Duis autem vel eum iriure dolor in hendrerit in vulputate velit esse molestie consequat, vel illum dolore eu feugiat .Ut wisi enim ad minim veniam, quis nostrud exerci tation ullamcorper suscipit lobortis nisl ut aliquip ex ea commodo consequat.</p>
  </article>
  <article class="abs post" style="top:659px">
    <div class="meta"><b>Det ampet</b> | June 5, 2014 3:26 am</div>
    <h3>VIDEO: Lorem ipsum dolor</h3>
    <p>Duis autem vel eum iriure dolor in hendrerit in vulputate velit esse molestie consequat, vel illum dolore eu feugiat Ut wisi enim ad minim veniam, quis nostrud exerci tation ullamcorper suscipit lobortis nisl ut aliquip ex ea commodo consequat.</p>
  </article>
  <article class="abs post" style="top:751px">
    <div class="meta"><b>Det ampet</b> | June 5, 2014 3:26 am</div>
    <h3>VIDEO: Lorem ipsum dolor</h3>
    <p>Duis autem vel eum iriure dolor in hendrerit in vulputate velit esse molestie consequat, vel illum dolore eu feugiat Ut wisi enim ad minim veniam, quis nostrud exerci tation ullamcorper suscipit lobortis nisl ut aliquip ex ea commodo consequat.</p>
  </article>
</main>

<section class="abs band">
  <h2>READY FOR AN IRREVERSIBLE &amp; ULTIMATE EXPERIENCE?</h2>
  <div class="abs band-btn">LET'S GET STARTED</div>
</section>

<footer>
  <div class="abs foot-brand"><span class="dot"></span>Lunaris Grove</div>
  <h3 class="abs recent-title">RECENT POSTS</h3>
  <div class="recent">
    <a style="left:493px;top:1020px">Curabitur ac neque at arcu</a>
    <a style="left:493px;top:1040px">Proin vel mauris diam</a>
    <a style="left:493px;top:1060px">Proin urna enim semper</a>
    <a style="left:493px;top:1080px">Nunc adipiscing semper nisl</a>
    <a style="left:644px;top:1020px">Curabitur ac neque at arcu</a>
    <a style="left:644px;top:1040px">Proin vel mauris diam</a>
    <a style="left:644px;top:1060px">Proin urna enim semper</a>
    <a style="left:644px;top:1080px">Nunc adipiscing semper nisl</a>
  </div>
  <div class="abs divider"></div>
  <div class="abs copy">Copyright © 2013 - All Rights Reserved</div>
  <nav class="foot-nav">
    <a class="on" style="left:413px">HOME</a>
    <a style="left:454px">LUNARIS GROVE</a>
    <a style="left:556px">BLOG</a>
    <a style="left:596px">OUR BIOS</a>
    <a style="left:653px">CONTACT US</a>
  </nav>
  <div class="social-foot" aria-label="Social links">
    <span style="left:727px;background:#3c64b1"></span>
    <span style="left:754px;background:#2ea3dc"></span>
    <span style="left:780px;background:#d3262b"></span>
  </div>
</footer>

</body>
</html>
```